Business Card for Olive Lotus-Eco Friendly Organic Clothing Brand

We are looking for an amazing business card for our eco friendly, organic clothing brand. We are thinking maybe a business card with a peel off sticker on the back, since our hanging clothing tag is a peel off sticker on the back. I will attach our hang tag so we can make sure we stay in line with our design. I've also attached a bag we are doing because I do like the scattered emblem look as well.

```html
<!DOCTYPE html>
<html lang="en">
<head>
<meta charset="utf-8">
<title>Olive Lotus – Business Card</title>
<link href="https://fonts.googleapis.com/css2?family=Open+Sans:wght@400;600;700&display=swap" rel="stylesheet">
<style>
  :root{
    --backdrop:#e4dccd;
    --card-white:#f7f7f5;
    --card-black:#0d0d0d;
    --magenta:#e0169a;
    --ink:#1d1d1d;
    --gold:#d8c25a;
    --muted-white:#e9e9e9;
  }
  *{box-sizing:border-box;margin:0;padding:0}
  html,body{width:1200px;height:780px;overflow:hidden}
  body{
    background:var(--backdrop);
    font-family:"Open Sans",Arial,sans-serif;
    position:relative;
  }
  .card{
    position:absolute;
    top:235px;
    width:540px;height:310px;
    border-radius:18px;
    box-shadow:0 6px 18px rgba(0,0,0,.18);
    overflow:hidden;
  }
  /* front */
  .card-front{left:30px;background:var(--card-white)}
  .brand-block{
    position:absolute;left:26px;top:158px;
    display:flex;align-items:center;gap:8px;
    white-space:nowrap;
  }
  .brand-mark{width:14px;height:14px;background:var(--magenta);flex:none}
  .brand-name{
    font-weight:700;font-size:27px;color:var(--magenta);line-height:1;
  }
  .rule-horizontal{
    position:absolute;left:232px;right:0;top:102px;height:1.5px;background:var(--magenta);
  }
  .rule-vertical{
    position:absolute;left:232px;top:102px;width:1.5px;height:150px;background:var(--magenta);
  }
  .person{position:absolute;left:254px;top:34px}
  .person-name{font-weight:700;font-size:28px;color:var(--magenta);line-height:1.1;white-space:nowrap}
  .person-role{font-size:15px;color:var(--ink);margin-top:4px}
  .contact-list{position:absolute;left:254px;top:122px;list-style:none}
  .contact-list li{
    display:flex;align-items:center;gap:8px;
    font-size:16px;color:var(--ink);height:28px;white-space:nowrap;
  }
  .contact-icon{
    width:20px;height:20px;border-radius:4px;background:var(--magenta);
    display:flex;align-items:center;justify-content:center;flex:none;
  }
  /* back */
  .card-back{left:630px;background:var(--card-black)}
  .hang-tag{position:absolute;left:70px;top:34px;width:400px;height:170px}
  .tag-name{
    position:absolute;left:164px;top:66px;
    font-weight:700;font-size:27px;color:var(--gold);line-height:1;white-space:nowrap;
  }
  .tag-url{
    position:absolute;left:164px;top:104px;
    font-size:12px;color:var(--muted-white);letter-spacing:.3px;white-space:nowrap;
  }
  .back-footer{
    position:absolute;left:0;right:0;bottom:30px;
    display:flex;align-items:center;justify-content:center;gap:22px;
  }
  .back-url{font-size:15px;font-weight:600;color:var(--muted-white)}
  .social-row{display:flex;gap:12px}
  .social-dot{width:22px;height:22px;border-radius:50%;border:1.5px solid var(--muted-white)}
</style>
</head>
<body>

  <section class="card card-front" aria-label="Card front">
    <div class="brand-block">
      <span class="brand-mark"></span>
      <span class="brand-name">Olive Lotus</span>
    </div>

    <div class="rule-horizontal"></div>
    <div class="rule-vertical"></div>

    <div class="person">
      <p class="person-name">Employee Name</p>
      <p class="person-role">Manager</p>
    </div>

    <ul class="contact-list">
      <li>Harbor Point, FL 33012</li>
      <li>
        <span class="contact-icon">
          <svg width="12" height="12" viewBox="0 0 24 24"><path fill="#fff" d="M6.6 10.8a15.1 15.1 0 0 0 6.6 6.6l2.2-2.2c.3-.3.7-.4 1-.2 1.1.4 2.3.6 3.6.6.6 0 1 .4 1 1V20c0 .6-.4 1-1 1A17 17 0 0 1 3 4c0-.6.4-1 1-1h3.5c.6 0 1 .4 1 1 0 1.3.2 2.5.6 3.6.1.3 0 .7-.2 1z"/></svg>
        </span>(555) 014-2290
      </li>
      <li>
        <span class="contact-icon">
          <svg width="12" height="12" viewBox="0 0 24 24"><path fill="none" stroke="#fff" stroke-width="2.4" d="M3 6h18v12H3z M3 6l9 7 9-7"/></svg>
        </span>hello@olivelotus-wear.com
      </li>
      <li>
        <span class="contact-icon">
          <svg width="12" height="12" viewBox="0 0 24 24"><circle cx="12" cy="12" r="9" fill="none" stroke="#fff" stroke-width="2"/><path fill="none" stroke="#fff" stroke-width="2" d="M3 12h18M12 3c3 3 3 15 0 18M12 3c-3 3-3 15 0 18"/></svg>
        </span>www.olivelotus-wear.com
      </li>
    </ul>
  </section>

  <section class="card card-back" aria-label="Card back">
    <div class="hang-tag">
      <svg width="400" height="170" viewBox="0 0 400 170">
        <defs>
          <linearGradient id="tagFill" x1="0" y1="0" x2="1" y2="1">
            <stop offset="0" stop-color="#3a4529"/>
            <stop offset="1" stop-color="#252d1b"/>
          </linearGradient>
          <linearGradient id="photoFill" x1="0" y1="0" x2="1" y2="1">
            <stop offset="0" stop-color="#6b7a45"/>
            <stop offset="1" stop-color="#2f3a22"/>
          </linearGradient>
        </defs>
        <rect x="20" y="22" width="370" height="130" rx="16" fill="url(#tagFill)" stroke="#d8c25a" stroke-width="3" role="img" aria-label="Camouflage pattern hang tag background"/>
        <circle cx="372" cy="87" r="5" fill="#bdbdbd"/>
        <rect x="4" y="6" width="140" height="140" fill="url(#photoFill)" stroke="#d8c25a" stroke-width="3" role="img" aria-label="Camouflage seated meditation figure emblem"/>
      </svg>
      <span class="tag-name">Olive Lotus</span>
      <span class="tag-url">www.olivelotus-wear.com</span>
    </div>

    <div class="back-footer">
      <span class="back-url">www.olivelotus-wear.com</span>
      <div class="social-row">
        <span class="social-dot"></span>
        <span class="social-dot"></span>
        <span class="social-dot"></span>
        <span class="social-dot"></span>
      </div>
    </div>
  </section>

</body>
</html>
```